Painting Company Business Card

Brightwell Painting needs a new business card. See attachments for our logo and current card as an example.
We want to utilize the same colors in the logo, and keep all the information that is currently on it. Just need an updated and modern design.
We are open to loosing the Association Logos if it means a better design.
We are also entertaining a spot for a picture of a headshot of the person listed on the card. Head shot can be finished later.

```html
<!DOCTYPE html>
<html lang="en">
<head>
<meta charset="utf-8">
<title>Brightwell Painting – Business Card</title>
<link href="https://fonts.googleapis.com/css2?family=Open+Sans:wght@400;600;700&display=swap" rel="stylesheet">
<style>
  :root{
    --maroon:#7a0606;
    --cyan:#4fd0f0;
    --olive:#4b6414;
    --magenta:#f021c6;
    --orange:#f7941d;
    --ink:#3b3b3b;
    --white:#ffffff;
    --page:#ffffff;
    --badge:#d9dde2;
  }
  *{box-sizing:border-box;margin:0;padding:0}
  html,body{width:1200px;height:1000px;overflow:hidden;background:var(--page)}
  body{position:relative;font-family:"Open Sans",Arial,sans-serif}
  .card{position:absolute;left:260px;width:720px;height:417px;background:var(--white);overflow:hidden;box-shadow:0 0 0 1px #e6e6e6}
  .card--front{top:55px}
  .card--back{top:518px}
  .card__art{position:absolute;inset:0;width:720px;height:417px}
  .brand-name{position:absolute;color:var(--olive);font-weight:700;line-height:1.02;letter-spacing:.5px}
  .card--front .brand-name{left:36px;top:150px;font-size:40px}
  .card--back .brand-name{left:452px;top:52px;font-size:40px}
  .brand-watermark{position:absolute;left:205px;top:118px;font-size:56px;font-weight:700;line-height:1.05;color:var(--olive);opacity:.05}
  .person{position:absolute;left:423px;top:58px;border-left:5px solid var(--cyan);padding-left:22px}
  .person__name{color:var(--white);font-size:26px;font-weight:700;line-height:1.1}
  .person__role{color:var(--white);font-size:17px;font-weight:400;margin-top:10px}
  .contact{position:absolute;color:var(--white);font-size:19px;font-weight:400;white-space:nowrap}
  .contact--phone{left:415px;top:228px}
  .contact--email{left:436px;top:268px}
  .contact--web{left:460px;top:312px}
  .services{position:absolute;left:55px;top:50px}
  .services__title{color:var(--olive);font-size:22px;font-weight:700;text-decoration:underline;text-underline-offset:3px}
  .services__list{list-style:none;margin-top:6px}
  .services__list li{color:var(--ink);font-size:23px;line-height:32.5px;position:relative;padding-left:22px}
  .services__list li::before{content:"";position:absolute;left:0;top:15px;width:6px;height:6px;border-radius:50%;background:var(--ink)}
  .paint-band{position:absolute;left:0;bottom:0}
  .card--front .paint-band{width:445px;height:40px;background:linear-gradient(90deg,var(--orange) 0%,var(--olive) 45%,var(--magenta) 100%)}
  .card--back .paint-band{width:720px;height:60px;background:linear-gradient(90deg,var(--magenta) 0%,var(--olive) 50%,var(--orange) 100%)}
</style>
</head>
<body>

<section class="card card--front" aria-label="Business card front">
  <div class="paint-band" role="img" aria-label="Decorative paint-stroke band in orange, green and pink"></div>
  <svg class="card__art" viewBox="0 0 720 417" aria-hidden="true">
    <polygon points="205,0 720,0 720,417 450,417" fill="var(--maroon)"/>
    <polygon points="195,0 215,0 457,417 440,417" fill="var(--cyan)"/>
    <polygon points="330,222 390,222 462,350 402,350" fill="var(--cyan)" stroke="var(--cyan)" stroke-width="14" stroke-linejoin="round"/>
    <g stroke="#e8c9c9" stroke-width="1" opacity=".8">
      <line x1="705" y1="233" x2="720" y2="233"/>
      <line x1="395" y1="258" x2="720" y2="258"/>
      <line x1="418" y1="300" x2="720" y2="300"/>
      <line x1="705" y1="327" x2="720" y2="327"/>
    </g>
    <g fill="var(--white)">
      <path d="M366,231 c2,-2 4,-2 5,0 l3,4 c1,1.5 0,3 -1.5,4 c1.5,3 4,5.5 7,7 c1,-1.5 2.5,-2.5 4,-1.5 l4,3 c2,1 2,3 0,5 c-3,3 -7,2 -12,-2 c-5,-4 -9,-9 -10,-13 c-1,-3 0,-5 0.5,-6.5 z"/>
      <rect x="383" y="273" width="24" height="16" rx="1.5"/>
      <path d="M383,274 l12,9 l12,-9" fill="none" stroke="var(--cyan)" stroke-width="2"/>
      <circle cx="423" cy="325" r="11" fill="none" stroke="var(--white)" stroke-width="2.2"/>
      <ellipse cx="423" cy="325" rx="4.5" ry="11" fill="none" stroke="var(--white)" stroke-width="2"/>
      <line x1="412" y1="325" x2="434" y2="325" stroke="var(--white)" stroke-width="2"/>
      <line x1="414" y1="319" x2="432" y2="319" stroke="var(--white)" stroke-width="1.6"/>
      <line x1="414" y1="331" x2="432" y2="331" stroke="var(--white)" stroke-width="1.6"/>
    </g>
  </svg>

  <div class="brand-name">Brightwell<br>Painting</div>

  <div class="person">
    <div class="person__name">Daniel Harper</div>
    <div class="person__role">Quality Manager</div>
  </div>

  <div class="contact contact--phone">262-555-0147</div>
  <div class="contact contact--email">Daniel.Brightwell@gmail.com</div>
  <div class="contact contact--web">BrightwellPainting.com</div>
</section>

<section class="card card--back" aria-label="Business card back">
  <div class="brand-watermark" aria-hidden="true">Brightwell<br>Painting</div>

  <svg class="card__art" viewBox="0 0 720 417" aria-hidden="true">
    <g fill="var(--badge)">
      <rect x="70" y="255" width="85" height="62" rx="4"/>
      <rect x="182" y="255" width="72" height="80" rx="4"/>
      <rect x="280" y="255" width="48" height="76" rx="4"/>
      <rect x="356" y="258" width="98" height="66" rx="4"/>
      <rect x="466" y="258" width="84" height="42" rx="4"/>
      <rect x="575" y="255" width="108" height="44" rx="4"/>
    </g>
  </svg>

  <div class="paint-band" role="img" aria-label="Decorative paint-stroke band in pink, green and orange"></div>

  <div class="services">
    <h2 class="services__title">OUR SERVICES</h2>
    <ul class="services__list">
      <li>Exterior Painting</li>
      <li>Interior Painting</li>
      <li>Carpentry</li>
      <li>Drywall</li>
    </ul>
  </div>

  <div class="brand-name">Brightwell<br>Painting</div>
</section>

</body>
</html>
```